Brave Otter Pet Sitting Postcard

I will be sending these postcards to homes in the neighborhood introducing my pet sitting business.

Include the following on the postcard:
Rosalind Hume
555-318-7294
www.braveotterpetsitting.example
help@braveotterpetsitting.example

```html
<!DOCTYPE html>
<html lang="en">
<head>
<meta charset="utf-8">
<title>Brave Otter Pet Sitting Postcard</title>
<link href="https://fonts.googleapis.com/css2?family=Delius&display=swap" rel="stylesheet">
<style>
  :root {
    --backdrop: #17a79e;
    --card-white: #ffffff;
    --band-dark: #231f20;
    --brand-red: #e2062a;
    --brand-orange: #f2a33a;
    --brand-yellow: #ffd23a;
    --ink: #1a1a1a;
  }
  * { margin: 0; padding: 0; box-sizing: border-box; }
  html, body {
    width: 1200px; height: 1200px; overflow: hidden;
    background: var(--backdrop);
    font-family: "Delius", "Comic Sans MS", sans-serif;
  }
  .postcard {
    position: absolute; left: 50px; top: 232px;
    width: 1150px; height: 770px;
    transform: scale(0.9565); transform-origin: 0 0;
    background: var(--card-white);
    overflow: hidden;
  }
  .postcard__top-band {
    position: absolute; left: 0; top: 0; width: 100%; height: 50px;
    background: var(--band-dark);
  }
  .brand-art {
    position: absolute; left: 103px; top: 127px; width: 300px; height: 300px;
    border-radius: 50%;
    background: radial-gradient(circle at 50% 40%, var(--brand-yellow), var(--brand-orange) 70%);
  }
  .brand-name {
    position: absolute; left: 20px; width: 460px; top: 454px;
    text-align: center; font-size: 34px; line-height: 1; color: var(--ink);
  }
  .tagline { position: absolute; color: var(--brand-orange); line-height: 1; white-space: nowrap; }
  .tagline--we { left: 663px; top: 98px; font-size: 40px; }
  .tagline--care { left: 753px; top: 68px; font-size: 80px; }
  .tagline--about { left: 676px; top: 134px; font-size: 100px; }
  .tagline--pet { left: 683px; top: 227px; font-size: 50px; }
  .contact {
    position: absolute; left: 510px; width: 620px; text-align: center;
    color: var(--brand-red); line-height: 1; white-space: nowrap;
  }
  .contact__call { top: 336px; font-size: 32px; }
  .contact__name { top: 390px; font-size: 58px; letter-spacing: 2px; }
  .contact__phone { top: 462px; font-size: 52px; letter-spacing: 2px; }
  .contact__phone .sep { font-size: 30px; vertical-align: 14px; }
  .info-band {
    position: absolute; left: 0; top: 604px; width: 100%; height: 166px;
    background: var(--brand-red); color: var(--card-white);
  }
  .info-band__email, .info-band__web {
    position: absolute; top: 24px; font-size: 29px; line-height: 1; letter-spacing: 0.5px; white-space: nowrap;
  }
  .info-band__email { left: 66px; }
  .info-band__web { left: 604px; }
  .info-band__credentials {
    position: absolute; top: 72px; left: 0; width: 100%;
    text-align: center; font-size: 24px; line-height: 1; letter-spacing: 1px;
  }
  .paw-trail {
    position: absolute; left: 0; bottom: 0; width: 100%; height: 60px;
    background: linear-gradient(90deg, rgba(242,120,40,.55), rgba(30,160,200,.45) 20%, rgba(226,6,42,0) 40%, rgba(226,6,42,0) 70%, rgba(245,150,30,.5) 80%, rgba(250,230,40,.6) 92%, rgba(190,220,60,.6));
  }
</style>
</head>
<body>
  <main class="postcard">
    <div class="postcard__top-band"></div>

    <div class="brand-art" role="img" aria-label="Illustration of a dog and cat in a house under a palm tree above water"></div>
    <p class="brand-name">Brave Otter Pet Sitting</p>

    <p class="tagline tagline--we">We</p>
    <p class="tagline tagline--care">care</p>
    <p class="tagline tagline--about">about</p>
    <p class="tagline tagline--pet">your pet!</p>

    <p class="contact contact__call">CONTACT US NOW</p>
    <p class="contact contact__name">ROSALIND HUME</p>
    <p class="contact contact__phone">555<span class="sep">●</span>318<span class="sep">●</span>7294</p>

    <section class="info-band">
      <div class="paw-trail" role="img" aria-label="Colourful paw print pattern"></div>
      <p class="info-band__email">help@braveotterpetsitting.example</p>
      <p class="info-band__web">www.braveotterpetsitting.example</p>
      <p class="info-band__credentials">Certified, Insured &amp; Bonded</p>
    </section>
  </main>
</body>
</html>
```